Fern Hollow Animal Hospital Postcard Design

I need a postcard for grand opening. The front of the card should have our business name and logo, below the logo I want to have a coupon for " Free office visit or $ 20 off of packages " for the first time clients.

I want to have the packages prices and details on the back of the postcard, the details of the packages are attached.

```html
<!DOCTYPE html>
<html lang="en">
<head>
<meta charset="UTF-8">
<title>Fern Hollow Animal Hospital – Grand Opening Postcard</title>
<link rel="stylesheet" href="https://fonts.googleapis.com/css2?family=Oswald:wght@200;300;400;500&display=swap">
<style>
  :root {
    --paper: #ffffff;
    --sky: #9fd3e6;
    --brand-blue: #2a9fd0;
    --leaf: #8cc63f;
    --ink: #231f20;
    --muted: #6d6e70;
    --gold: #c9a46a;
    --gold-soft: #d9bb86;
    --ribbon: #c4161c;
    --ribbon-dark: #8e0f14;
    --fur-light: #c9935a;
    --fur-dark: #2b2622;
  }
  * { margin: 0; padding: 0; box-sizing: border-box; }
  html, body { width: 1200px; height: 600px; overflow: hidden; background: var(--paper); }
  .postcard {
    position: relative;
    width: 1200px;
    height: 600px;
    overflow: hidden;
    background: var(--paper);
    font-family: "Oswald", sans-serif;
    color: var(--ink);
  }
  .headline {
    position: absolute;
    left: 44px;
    top: 6px;
    font-weight: 200;
    font-size: 124px;
    line-height: 1;
    letter-spacing: 2px;
    color: var(--sky);
    white-space: nowrap;
    z-index: 2;
  }
  .pet-photo {
    position: absolute;
    left: 560px;
    top: 90px;
    width: 590px;
    height: 560px;
    border-radius: 48% 48% 0 0 / 40% 40% 0 0;
    background: radial-gradient(ellipse at 50% 35%, var(--fur-light) 0%, #9c6a3c 45%, var(--fur-dark) 85%);
    z-index: 1;
  }
  .event-info {
    position: absolute;
    left: 1004px;
    top: 30px;
    z-index: 3;
  }
  .event-date { font-weight: 400; font-size: 30px; line-height: 1.1; color: var(--brand-blue); }
  .event-time { font-weight: 400; font-size: 31px; line-height: 1.15; color: var(--leaf); }
  .event-address { font-weight: 400; font-size: 16px; letter-spacing: 0.5px; color: var(--leaf); margin-top: 2px; }
  .website {
    position: absolute;
    left: 974px;
    top: 310px;
    font-size: 11px;
    letter-spacing: 3px;
    color: var(--ink);
    z-index: 3;
  }
  .brand {
    position: absolute;
    left: 76px;
    top: 180px;
    display: flex;
    align-items: center;
    gap: 16px;
    z-index: 3;
  }
  .brand-mark { width: 86px; height: 86px; background: var(--leaf); }
  .brand-name {
    font-weight: 500;
    font-size: 36px;
    line-height: 1.05;
    color: var(--brand-blue);
    text-transform: uppercase;
  }
  .accent-block {
    position: absolute;
    left: 0;
    top: 422px;
    width: 300px;
    height: 178px;
    background: var(--leaf);
    z-index: 1;
  }
  .coupon {
    position: absolute;
    left: 108px;
    top: 308px;
    width: 494px;
    height: 236px;
    background: var(--paper);
    border: 2px solid var(--gold);
    border-radius: 16px;
    transform: rotate(-4deg);
    box-shadow: 0 4px 10px rgba(0,0,0,0.15);
    z-index: 2;
  }
  .coupon-ribbon {
    position: absolute;
    left: -8px;
    top: -28px;
    width: 190px;
    height: 170px;
    border-radius: 30px;
    background: linear-gradient(135deg, var(--ribbon) 0%, var(--ribbon-dark) 100%);
  }
  .offer-free {
    position: absolute;
    left: 218px;
    top: 70px;
    text-align: left;
  }
  .offer-free .big { font-weight: 500; font-size: 56px; line-height: 0.95; letter-spacing: -1px; }
  .offer-free .small { font-weight: 500; font-size: 21px; line-height: 1.1; }
  .offer-or {
    position: absolute;
    left: 306px;
    top: 76px;
    font-size: 12px;
    color: var(--muted);
    z-index: 1;
  }
  .offer-discount {
    position: absolute;
    left: 300px;
    top: 50px;
    width: 128px;
    height: 128px;
    border-radius: 50%;
    background: radial-gradient(circle at 40% 35%, var(--gold-soft), var(--gold));
  }
  .offer-discount-text {
    position: absolute;
    left: 328px;
    top: 62px;
    white-space: nowrap;
  }
  .offer-discount-text .big { font-weight: 500; font-size: 48px; line-height: 1; letter-spacing: -1px; }
  .offer-discount-text .big sup { font-size: 26px; vertical-align: 16px; }
  .offer-discount-text .big span { font-size: 26px; }
  .offer-discount-text .small { font-weight: 500; font-size: 21px; line-height: 1.1; }
  .offer-terms {
    position: absolute;
    left: 230px;
    top: 176px;
    font-weight: 300;
    font-size: 12px;
    letter-spacing: 1px;
    color: var(--muted);
  }
</style>
</head>
<body>
  <main class="postcard">
    <h1 class="headline">GRAND OPENING</h1>

    <div class="pet-photo" role="img" aria-label="Photo of a small long-haired terrier dog looking up"></div>

    <div class="event-info">
      <p class="event-date">SEPTEMBER 13</p>
      <p class="event-time">12PM - 4PM</p>
      <p class="event-address">ADRESS&nbsp;&nbsp;STREET 12345</p>
    </div>

    <p class="website">WWW.FERNHOLLOWVETS.COM</p>

    <div class="brand">
      <div class="brand-mark"></div>
      <p class="brand-name">Fern Hollow<br>Animal Hospital</p>
    </div>

    <div class="accent-block"></div>

    <section class="coupon">
      <div class="coupon-ribbon" role="img" aria-label="Red gift ribbon tied in a bow across the coupon corner"></div>
      <div class="offer-discount"></div>
      <div class="offer-free">
        <p class="big">FREE</p>
        <p class="small">OFFICE VISIT</p>
      </div>
      <p class="offer-or">OR</p>
      <div class="offer-discount-text">
        <p class="big"><sup>$</sup>20<span>OFF</span></p>
        <p class="small">OF PACKAGES</p>
      </div>
      <p class="offer-terms">FOR THE FIRST TIME CLIENTS.</p>
    </section>
  </main>
</body>
</html>
```